Postcard Design

We are a church and are having a large outreach event for our community. We are having a 50,000 easter egg hunt. We will have 25 bounce houses, free food and drinks. We need a card that is catching to the eye. We need a postcard design that is kid friendly yet shows how big this event will be. Bright colors, cool graphics and ultimately when parents and kids see this card they think "i need to be at this event". we are going to pass out 2000. on the front is the cool stuff and the main theme 50000 EGGS. ON the back location of event - Rolf Everby Athletic Park (3400 E. Tamsworth) contact Greg Whitlow - 575-208-4719 - Time 11:00am to 2:00pm - date Saturday April 3rd. Who all families and kids ages birth to 5th grade. EVERYTHING IS FREE. I am uploading 2 images that need to be on the back or front and not real big, our church logos.
Updates

Project Deadline Extended
Reason: Still waiting for the right one. Getting better and liking what i see. Thanks for all your hard work, just need a little more time

Industry/Entity Type

Church

```html
<!DOCTYPE html>
<html lang="en">
<head>
<meta charset="utf-8">
<title>Easter Outreach Postcard – Back</title>
<link href="https://fonts.googleapis.com/css2?family=Marcellus&family=Delius&family=Fredoka:wght@600;700&family=Lilita+One&display=swap" rel="stylesheet">
<style>
  :root {
    --paper: #ffffff;
    --magenta: #e6168a;
    --sun: #fdd800;
    --ink: #111111;
    --white: #ffffff;
    --sky: #29a8e0;
    --rule: #ececec;
  }
  * { margin: 0; padding: 0; box-sizing: border-box; }
  html, body { width: 1200px; height: 930px; overflow: hidden; background: var(--paper); }
  .postcard { position: relative; width: 1200px; height: 930px; }
  .postcard__art { position: absolute; inset: 0; }
  .block { position: absolute; line-height: 1.2; }

  .heading {
    font-family: "Lilita One", sans-serif;
    color: var(--ink);
    letter-spacing: 1px;
  }
  .info-title { left: 75px; top: 62px; font-size: 34px; }
  .info-line {
    left: 73px;
    font-family: "Delius", cursive;
    font-size: 23px;
    color: var(--white);
    white-space: nowrap;
  }
  .info-line b { font-weight: 700; }
  .info-line--venue { top: 110px; }
  .info-line--time { top: 148px; }
  .info-line--date { top: 187px; }

  .brand { display: flex; align-items: center; gap: 6px;
    font-family: "Delius", cursive; font-size: 15px; color: var(--white); white-space: nowrap; }
  .brand__mark { width: 14px; height: 14px; background: var(--white); flex: none; }
  .brand--church { left: 686px; top: 208px; }
  .brand--kids { left: 686px; top: 236px; }

  .welcome-title {
    left: 70px; top: 280px;
    font-family: "Marcellus", serif;
    font-size: 80px; line-height: 1;
    color: var(--ink);
    letter-spacing: 1px;
  }
  .welcome-families { left: 75px; top: 360px; font-family: "Delius", cursive; font-size: 28px; color: var(--ink); }
  .welcome-kids { left: 75px; top: 394px; font-family: "Delius", cursive; font-size: 19px; color: var(--ink); white-space: nowrap; }
  .welcome-kids strong { font-size: 27px; font-weight: 400; }

  .free-line1 { left: 70px; top: 478px; font-family: "Fredoka", sans-serif; font-weight: 700;
    font-size: 48px; line-height: 1; color: var(--magenta); letter-spacing: 1px; }
  .free-line2 { left: 146px; top: 530px; font-family: "Fredoka", sans-serif; font-weight: 700; line-height: 1; white-space: nowrap; }
  .free-line2 .is { font-size: 52px; color: var(--sky); margin-right: 22px; }
  .free-line2 .free { font-size: 66px; color: var(--ink); letter-spacing: 2px; }

  .contact-title { left: 73px; top: 660px; font-size: 36px; }
  .contact-line { left: 73px; top: 702px; font-family: "Delius", cursive; font-size: 25px; color: var(--white); white-space: nowrap; }
  .contact-line b { font-family: "Fredoka", sans-serif; font-weight: 600; letter-spacing: 1px; }
</style>
</head>
<body>
<main class="postcard">
  <svg class="postcard__art" width="1200" height="930" viewBox="0 0 1200 930">
    <polygon role="img" aria-label="Magenta swirl pattern background"
      points="0,0 895,0 895,290 575,290 575,762 0,762" fill="var(--magenta)"/>
    <path role="img" aria-label="Yellow swirl pattern blob"
      d="M0,340 C10,270 60,255 140,262 C240,270 300,225 390,222 C480,220 548,250 556,320
         C562,390 560,440 520,480 C480,520 470,560 462,595 C452,625 400,628 330,615
         C250,602 180,612 110,630 C60,642 20,648 0,645 Z" fill="var(--sun)"/>
    <path d="M895,0 V290 H575 V762 H0" fill="none" stroke="var(--ink)" stroke-width="5" stroke-dasharray="16 9"/>
    <g fill="var(--rule)">
      <rect x="637" y="460" width="468" height="7"/>
      <rect x="637" y="525" width="468" height="7"/>
      <rect x="637" y="591" width="468" height="7"/>
      <rect x="637" y="657" width="468" height="7"/>
      <rect x="637" y="722" width="468" height="7"/>
    </g>
  </svg>

  <h2 class="block heading info-title">INFO</h2>
  <p class="block info-line info-line--venue"><b>Venue</b> : Rolf Everby Athletic Park (3400 E. Tamsworth)</p>
  <p class="block info-line info-line--time"><b>Time</b> : 11:00am to 2:00pm</p>
  <p class="block info-line info-line--date"><b>Date</b> : Saturday April 3rd</p>

  <div class="block brand brand--church"><span class="brand__mark"></span>Grace Harbor Church</div>
  <div class="block brand brand--kids"><span class="brand__mark"></span>Harbor Kids</div>

  <h1 class="block welcome-title">WELCOME</h1>
  <p class="block welcome-families">All Families</p>
  <p class="block welcome-kids">and <strong>kids</strong> (age birth till 5th grade}</p>

  <p class="block free-line1">EVERYTHING</p>
  <p class="block free-line2"><span class="is">IS</span><span class="free">FREE</span></p>

  <h2 class="block heading contact-title">CONTACT</h2>
  <p class="block contact-line"><b>GREG WHITLOW</b> : 575-208-4719</p>
</main>
</body>
</html>
```